KB Sports & Remedial Massage needs a new logo & business card design

The design is for my Sports and remedial massage business. My business is aimed at everyone who has a muscle ache or injury so not just sports related. I need a design which is sharp, clear and professional. No greens, or pastel colours or floral/girly designs. Perhaps just a Navy background and white text or other way around or perhaps grey. I want to make it clear that I treat everyone and not just sporty people.

Target Market(s)

People with muscle aches or sports injuries

Industry/Entity Type

Health And Wellness

Contact Information for Business Card

It needs to also include the following:
Name: Megan Hartwell
Mobile No: 07493 215 648
Email: meganhartwell@parcelnet.example
Qualifications: Dip SM, Dip SRM

Logo Text

KB Sports & Remedial Massage

Font styles to use
Serif
Other font styles liked:
• Tahoma, Verdana

Colors
5c5c5c
7f7f7f
9d9d9d
0255a3
3176b5
85abd2

Requirements
Must have
• I was thinking of a few simple people figures at the bottom of the card to highlight this i.e. a gardener, musician mixed in with a cyclist and tennis player.
Should not have
• Anything which indicates beauty therapy or relaxing. I am there to get rid of aches and pains and often to give rehab to certain injuries.

```html
<!DOCTYPE html>
<html lang="en">
<head>
<meta charset="utf-8">
<title>KB Sports &amp; Remedial Massage Business Card</title>
<link rel="stylesheet" href="https://fonts.googleapis.com/css2?family=Lato:wght@400;700&display=swap">
<style>
  :root {
    --page-bg: #e9e6e2;
    --navy-top: #3176b5;
    --navy-bottom: #0255a3;
    --card-grey: #7f7f7f;
    --ring-grey: #5c5c5c;
    --soft-grey: #9d9d9d;
    --white: #ffffff;
    --shadow: rgba(0, 0, 0, 0.18);
  }
  * { box-sizing: border-box; margin: 0; padding: 0; }
  html, body { width: 1200px; height: 900px; overflow: hidden; }
  body {
    position: relative;
    background: var(--page-bg);
    font-family: "Lato", Tahoma, Verdana, sans-serif;
    color: var(--white);
  }
  .card {
    position: absolute;
    height: 343px;
    box-shadow: 0 6px 18px var(--shadow);
    overflow: hidden;
  }
  /* Front card */
  .card-front { left: 238px; top: 62px; width: 555px; background: var(--card-grey); }
  .front-panel {
    position: absolute; left: 0; top: 0; width: 395px; height: 100%;
    background: linear-gradient(180deg, var(--navy-top), var(--navy-bottom));
  }
  .front-divider {
    position: absolute; left: 395px; top: 0; width: 8px; height: 100%;
    background: var(--white);
  }
  .holder-name { position: absolute; left: 40px; top: 34px; font-size: 22px; font-weight: 700; }
  .holder-title { position: absolute; left: 40px; top: 63px; font-size: 15px; }
  .qualifications { position: absolute; left: 41px; top: 146px; font-size: 15px; line-height: 18px; }
  .contacts { position: absolute; left: 44px; top: 199px; list-style: none; font-size: 15px; }
  .contacts li { display: flex; align-items: center; height: 20px; white-space: nowrap; }
  .contacts svg { width: 10px; height: 10px; margin-right: 9px; fill: var(--white); flex: none; }
  .front-badge {
    position: absolute; left: 287px; top: 60px; width: 222px; height: 222px;
  }
  .front-badge svg { position: absolute; inset: 0; }
  .front-badge .brand-name {
    position: absolute; inset: 0; display: flex; align-items: center; justify-content: center;
    text-align: center; font-size: 19px; line-height: 24px; font-weight: 700;
    color: var(--ring-grey);
  }
  /* Back card */
  .card-back { left: 458px; top: 518px; width: 559px; background: var(--card-grey); }
  .back-ring {
    position: absolute; left: 191px; top: 66px; width: 158px; height: 158px;
    border: 5px solid var(--white); border-radius: 50%;
  }
  .back-name {
    position: absolute; left: 0; right: 0; top: 236px; text-align: center;
    font-size: 28px; font-weight: 700; white-space: nowrap;
  }
</style>
</head>
<body>
  <section class="card card-front">
    <div class="front-panel">
      <h1 class="holder-name">Megan Hartwell</h1>
      <p class="holder-title">Sports &amp; Remedial Massage Therapist</p>
      <p class="qualifications">Dip SM, Dip SRM</p>
      <ul class="contacts">
        <li><svg viewBox="0 0 10 10"><path d="M2.5 0h5v10h-5z M3.5 1v7h3V1z" fill-rule="evenodd"/></svg>07493 215 648</li>
        <li><svg viewBox="0 0 10 10"><path d="M0 2h10v6H0z M0.8 2.6L5 5.6l4.2-3" fill-rule="evenodd"/></svg>meganhartwell@parcelnet.example</li>
      </ul>
    </div>
    <div class="front-divider"></div>
    <div class="front-badge">
      <svg viewBox="0 0 222 222" width="222" height="222" aria-hidden="true">
        <circle cx="111" cy="111" r="111" fill="#ffffff"/>
        <circle cx="111" cy="111" r="100" fill="#ffffff" stroke="#5c5c5c" stroke-width="8"/>
      </svg>
      <span class="brand-name">KB Sports &amp;<br>Remedial<br>Massage</span>
    </div>
  </section>

  <section class="card card-back">
    <div class="back-ring"></div>
    <p class="back-name">KB Sports &amp; Remedial Massage</p>
  </section>
</body>
</html>
```